Velora Beauty Clinic

I need a web design for a Cosmetic Surgery Clinic. The current site is velora-beauty-clinic.example. The design should be:
- Flat Design with big banner
- Warm colors
- Responsive Layout
- SEO friendly

Cosmetic

```html
<!DOCTYPE html>
<html lang="en">
<head>
<meta charset="utf-8">
<title>Velora Beauty Clinic</title>
<link href="https://fonts.googleapis.com/css2?family=Open+Sans:ital,wght@0,300;0,400;0,600;0,700;1,400&display=swap" rel="stylesheet">
<style>
:root{
  --pink:#df62ad;
  --pink-dark:#c94e98;
  --ink:#2b2b2b;
  --text:#666;
  --muted:#999;
  --line:#e4e4e4;
  --paper:#fff;
  --band:#f3f3f3;
  --field:#fff;
  --footer:#1f1f1f;
  --dark-btn:#2a2a2a;
}
*{box-sizing:border-box;margin:0;padding:0}
html,body{width:1200px;height:2769px;overflow:hidden}
body{font-family:"Open Sans",Arial,sans-serif;color:var(--text);background:var(--paper);position:relative}
.abs{position:absolute}
.btn{position:absolute;background:var(--pink);color:#fff;font-size:10px;font-weight:600;text-transform:uppercase;display:flex;align-items:center;justify-content:center;letter-spacing:.3px}
.btn.dark{background:var(--dark-btn)}
.section-title{position:absolute;left:0;width:1200px;text-align:center;color:var(--ink);font-size:24px;font-weight:400}

/* header */
.site-header{position:absolute;top:0;left:0;width:1200px;height:92px;border-top:3px solid var(--pink);background:#fff;border-bottom:1px solid var(--line)}
.brand{position:absolute;left:161px;top:29px;font-size:21px;color:var(--pink);font-weight:600;letter-spacing:.2px}
.main-nav{position:absolute;left:535px;top:-3px;height:92px;display:flex}
.main-nav a{display:flex;align-items:center;padding:0 20px;font-size:11px;color:#555;text-decoration:none;text-transform:uppercase;letter-spacing:.3px}
.main-nav a.active{background:var(--pink);color:#fff;padding:0 16px}

/* hero */
.hero{position:absolute;top:92px;left:0;width:1200px;height:565px;background:linear-gradient(100deg,#e8d9cf 0%,#f0e2d6 30%,#f6efe8 55%,#eeece8 80%,#dfe4d8 100%)}
.hero-title{position:absolute;left:698px;top:203px;font-size:30px;color:var(--ink);font-weight:400}
.hero-title b{color:var(--pink);font-weight:600}
.hero-sub{position:absolute;left:695px;top:258px;width:400px;font-size:15px;font-style:italic;color:#555;line-height:24px}
.slider-dots{position:absolute;left:538px;top:532px;display:flex;gap:6px}
.slider-dots span{width:24px;height:3px;background:#333}
.slider-dots span.on{background:var(--pink)}

/* intro */
.intro-lead{position:absolute;left:300px;top:722px;width:600px;text-align:center;font-style:italic;color:var(--pink);font-size:14px;line-height:20px}
.rule{position:absolute;left:258px;top:800px;width:684px;height:1px;background:var(--line)}
.holiday-text{position:absolute;left:225px;top:890px;width:750px;text-align:center;font-size:12.5px;line-height:20px;color:#555}

/* treatments */
.treatments{position:absolute;top:1030px;left:0;width:1200px;height:560px;background:var(--band)}
.card{position:absolute;top:103px;width:264px;height:399px;background:#fff}
.card .photo{height:224px}
.card h3{margin-top:18px;text-align:center;font-size:17px;font-weight:400;color:var(--ink)}
.card ul{list-style:none;margin-top:12px;text-align:center;font-size:11px;line-height:19px;color:#666}
.card .btn{left:77px;top:349px;width:111px;height:30px}

/* testimonial */
.testimonial{position:absolute;top:1590px;left:0;width:1200px;height:234px;background:var(--pink);color:#fff}
.quote-badge{position:absolute;left:567px;top:20px;width:66px;height:66px;border-radius:50%;background:var(--pink-dark);display:flex;align-items:center;justify-content:center}
.testimonial blockquote{position:absolute;left:320px;top:106px;width:560px;text-align:center;font-style:italic;font-size:15.5px;line-height:24px}
.testimonial cite{position:absolute;left:0;top:172px;width:1200px;text-align:center;font-size:13px;font-style:italic}
.t-dots{position:absolute;left:560px;top:203px;display:flex;gap:4px}
.t-dots span{width:9px;height:9px;border:1px solid #fff;border-radius:50%}
.t-dots span.on{background:#fff}

/* blog */
.post{position:absolute;top:1920px;width:270px}
.post .photo{height:177px;position:relative}
.date{position:absolute;left:0;top:0;width:61px;height:48px;background:var(--pink);color:#fff;text-align:center}
.date strong{display:block;font-size:22px;line-height:26px;font-weight:600;padding-top:2px}
.date small{display:block;font-size:8px}
.tag{position:absolute;left:0;top:48px;width:61px;height:42px;background:#e9e9e9;display:flex;align-items:center;justify-content:center}
.post h4{margin-top:18px;font-size:14.5px;font-weight:400;color:var(--ink)}
.post p{margin-top:8px;font-size:11px;line-height:18px;color:#777}
.post .btn{position:static;margin-top:10px;width:111px;height:30px}

/* contact */
.contact-band{position:absolute;top:2293px;left:0;width:1200px;height:389px;background:var(--band)}
.block-title{position:absolute;top:32px;font-size:23px;font-weight:400;color:var(--ink)}
.field{position:absolute;background:var(--field);font-size:11px;color:#777;padding:10px 12px}
.field i{color:var(--pink);font-style:normal}
.experience p{position:absolute;font-size:11px;line-height:19px;color:#666}
.experience em{color:var(--pink)}

/* footer */
.site-footer{position:absolute;top:2682px;left:0;width:1200px;height:87px;background:var(--footer);color:#ccc}
.foot-nav{position:absolute;left:161px;top:25px;font-size:9.5px;text-transform:uppercase;letter-spacing:.2px}
.foot-nav span{margin:0 6px;color:#777}
.copy{position:absolute;left:161px;top:50px;font-size:9.5px;color:#999}
.social{position:absolute;left:825px;top:26px;display:flex;gap:9px}
.social span{width:36px;height:36px;border:1px solid #bbb;display:block}
</style>
</head>
<body>

<header class="site-header">
  <div class="brand">Velora Beauty Clinic</div>
  <nav class="main-nav">
    <a class="active">Home</a><a>Services</a><a>Gallery</a><a>Testimonials</a><a>Staff</a><a>News</a><a>Contact</a>
  </nav>
</header>

<section class="hero" role="img" aria-label="Banner photo: surgeon marking a patient for body plastic surgery in a bright clinic room">
  <h1 class="hero-title"><b>BODY PLASTIC</b> SURGERY</h1>
  <p class="hero-sub">Velora Beauty Clinic offers a range of plastic &amp; reconstructive surgery options at affordable</p>
  <div class="slider-dots"><span class="on"></span><span></span><span></span><span></span></div>
</section>

<h2 class="section-title" style="top:680px">Face, Body, Breast Plastic Surgery</h2>
<p class="intro-lead">Velora Beauty Clinic offers a range of plastic and reconstructive surgery options at affordable prices for those considering medical tourism abroad.</p>
<div class="rule"></div>

<h2 class="section-title" style="top:840px">Cosmetic Surgery Holiday Packages in Cyprus</h2>
<p class="holiday-text">If you are considering medical tourism, Velora Beauty Clinic can offer you tailor made affordable cosmetic surgery holiday packages in Cyprus including accommodation and travel arrangements that suit your specific needs. We offer you top quality cosmetic surgery procedures abroad at affordable cosmetic surgery prices with dedicated aftercare.</p>
<div class="btn" style="left:556px;top:967px;width:89px;height:30px">Read More</div>

<section class="treatments">
  <h2 class="section-title" style="top:28px">Aesthetic Plastic Surgery Treatments</h2>
  <article class="card" style="left:161px">
    <div class="photo" role="img" aria-label="Photo for face plastic surgery" style="background:linear-gradient(135deg,#f1e6e0,#e9cfc4)"></div>
    <h3>Face Plastic Surgery</h3>
    <ul><li>Eyelid Surgery – From £950</li><li>Facelift (inc neck and cheek) – £2400</li><li>Rhinoplasty (inc Septoplasty) – £1800</li></ul>
    <div class="btn">Read More</div>
  </article>
  <article class="card" style="left:469px">
    <div class="photo" role="img" aria-label="Photo for breast plastic surgery" style="background:linear-gradient(135deg,#ece5e2,#d9b9a8)"></div>
    <h3>Breast Plastic Surgery</h3>
    <ul><li>Eyelid Surgery – From £950</li><li>Facelift (inc neck and cheek) – £2400</li><li>Rhinoplasty (inc Septoplasty) – £1800</li></ul>
    <div class="btn">Read More</div>
  </article>
  <article class="card" style="left:774px">
    <div class="photo" role="img" aria-label="Photo for body plastic surgery" style="background:linear-gradient(180deg,#e6c6b3,#efe6e2)"></div>
    <h3>Body Plastic Surgery</h3>
    <ul><li>Eyelid Surgery – From £950</li><li>Facelift (inc neck and cheek) – £2400</li><li>Rhinoplasty (inc Septoplasty) – £1800</li></ul>
    <div class="btn">Read More</div>
  </article>
</section>

<section class="testimonial">
  <div class="quote-badge">
    <svg width="30" height="24" viewBox="0 0 30 24"><path fill="#fff" d="M2 24V13C2 6 6 2 12 1v4c-3 1-5 3-5 7h5v12zM18 24V13c0-7 4-11 10-12v4c-3 1-5 3-5 7h5v12z"/></svg>
  </div>
  <blockquote>“Fusce dapibus, tellus ac cursus commodo, tortor mauris condimentum. Duis mollis, est non commodo luctus, nisi erat ”</blockquote>
  <cite>Elena – Breast Lift with Implants</cite>
  <div class="t-dots"><span></span><span></span><span class="on"></span><span></span><span></span><span></span></div>
</section>

<h2 class="section-title" style="top:1851px">Cosmetic Surgery Blog</h2>
<article class="post" style="left:161px">
  <div class="photo" role="img" aria-label="Blog photo: facial treatment" style="background:linear-gradient(135deg,#e4e2e2,#d8bfb0)">
    <div class="date"><strong>17</strong><small>29,2015</small></div>
    <div class="tag"><svg width="14" height="14" viewBox="0 0 14 14"><path fill="var(--pink)" d="M10 1l3 3-7 7-4 1 1-4z"/></svg></div>
  </div>
  <h4>A Guide To Cosmetic Surgery in Cyprus</h4>
  <p>You can save money. Cosmetic surgery is not classified as a medical necessity in most healthcare systems, so most people have to pay for their treatment.their</p>
  <div class="btn dark">Read More</div>
</article>
<article class="post" style="left:464px">
  <div class="photo" role="img" aria-label="Blog photo: breast surgery consultation" style="background:linear-gradient(135deg,#e6dcd6,#cdb0a0)">
    <div class="date"><strong>17</strong><small>29,2015</small></div>
    <div class="tag"><svg width="14" height="14" viewBox="0 0 14 14"><path fill="var(--pink)" d="M10 1l3 3-7 7-4 1 1-4z"/></svg></div>
  </div>
  <h4>A Guide To Cosmetic Surgery in Cyprus</h4>
  <p>You can save money. Cosmetic surgery is not classified as a medical necessity in most healthcare systems, so most people have to pay for their treatment.their</p>
  <div class="btn dark">Read More</div>
</article>
<article class="post" style="left:768px">
  <div class="photo" role="img" aria-label="Blog photo: body contour markings" style="background:linear-gradient(135deg,#dcdad9,#c9a894)">
    <div class="date"><strong>17</strong><small>29,2015</small></div>
    <div class="tag"><svg width="14" height="14" viewBox="0 0 14 14"><path fill="var(--pink)" d="M10 1l3 3-7 7-4 1 1-4z"/></svg></div>
  </div>
  <h4>A Guide To Cosmetic Surgery in Cyprus</h4>
  <p>You can save money. Cosmetic surgery is not classified as a medical necessity in most healthcare systems, so most people have to pay for their treatment.their</p>
  <div class="btn dark">Read More</div>
</article>

<section class="contact-band">
  <h3 class="block-title" style="left:161px">Contact Us</h3>
  <div class="field" style="left:161px;top:87px;width:219px;height:32px">Name <i>*</i></div>
  <div class="field" style="left:393px;top:87px;width:220px;height:32px">Phone<i>*</i></div>
  <div class="field" style="left:161px;top:131px;width:219px;height:32px">Email address<i>*</i></div>
  <div class="field" style="left:393px;top:131px;width:220px;height:32px">Subject <i>*</i></div>
  <div class="field" style="left:161px;top:173px;width:452px;height:113px">Your message<i>*</i></div>
  <div class="btn" style="left:161px;top:310px;width:110px;height:30px">Send Message</div>

  <div class="experience">
    <h3 class="block-title" style="left:679px">Our Experience Shows</h3>
    <div class="abs" role="img" aria-label="Portrait of the lead surgeon" style="left:679px;top:88px;width:120px;height:124px;background:linear-gradient(160deg,#b7c7d6,#8a6b5a)"></div>
    <p style="left:816px;top:90px;width:226px">If you are considering cosmetic surgery abroad look no further. Plastic surgery abroad is an opportunity to give a desired area of your body a new and improved look. At <em>Velora Beauty Clinic</em>, we promise to deliver the best plastic surgery options.</p>
    <p style="left:679px;top:232px;width:363px"><em>Velora Beauty</em> Clinic specialises in facial, breast and body cosmetic and reconstructive surgeries. We have performed plastic surgery for more than 25 years</p>
    <div class="btn" style="left:679px;top:310px;width:111px;height:30px">Read More</div>
  </div>
</section>

<footer class="site-footer">
  <nav class="foot-nav">Home<span>|</span>About Us<span>|</span>Our Services<span>|</span>Health<span>|</span>News<span>|</span>Testimonials<span>|</span>Other Services<span>|</span>Contact Us</nav>
  <div class="copy">© 2015 all copy rights are reserved . velora-beauty-clinic.example</div>
  <div class="social"><span></span><span></span><span></span><span></span><span></span></div>
</footer>

</body>
</html>
```